Web Design Project

i'm looking for a sleek modern design i can use for a web site that deals with.
Intelligent Data Capture
Accounts Payable Solutions for faster processing based on our scanning solution.
ultimately we are a intelligent scanning software.

here is a great website, that does exactly what we do, and we like to have most of their services and products.

so something in this idea would be great.
www.dravolin.com

so i guess i want a good landing/home page which is smartly designed so users will be inclined to leave their information.

and then information pages.

also i dont need any cms for you to include, i only need you to hook the html hooks for RANK Kettle as i already have a CMS and need it to hook in to that, i am including links to that cheat sheet.
so it is easier when included as you create the Theme.

http://www.rankkettle.com/how-to-create-website-template.html
http://www.rankkettle.com/cheat-sheet.html
Updates

Hi Guys sorry for the long pause in design, but here is where we stand.

what ever design i choose, i need that designer to customize a few things for me based on design that was designed.
and i will need designer to match that them to work with RANK Kettle
here is the cheat sheet for the hooks that we need to match and make it work.
if you have any questions let me know.

otherwise i look forward to working with you. and good luck.

Target Market(s)

CFO's AP Managers, mostly ppl who are not Tech freindly

Industry/Entity Type

Software

Requirements
Must have
• i need on home page, the rotating banner should have 1 ability to place vidmora links to show videos, and also ability to add buttons on these rotating banners that will allow forms to pop up take to another page.

```html
<!DOCTYPE html>
<html lang="en">
<head>
<meta charset="utf-8">
<title>KORVA – Intelligent Data Capture</title>
<link href="https://fonts.googleapis.com/css2?family=Ubuntu:wght@400;500&family=Arimo:wght@400;700&display=swap" rel="stylesheet">
<style>
:root{
  --blue:#1e7fb1;
  --blue-dark:#0f5f8c;
  --blue-light:#4aa6d3;
  --blue-pale:#e8f3f9;
  --ink:#222;
  --muted:#6a6a6a;
  --line:#d6d6d6;
  --page:#f3f3f3;
  --card:#f6f6f6;
  --footer:#3b3b3b;
  --white:#fff;
}
*{box-sizing:border-box;margin:0;padding:0}
html,body{width:1079px;height:1200px;overflow:hidden}
body{position:relative;background:var(--page);font-family:"Arimo",Arial,sans-serif;color:var(--ink)}
.topline{position:absolute;left:0;top:0;width:1079px;height:7px;background:var(--blue-dark)}
.header{position:absolute;left:0;top:7px;width:1079px;height:112px;background:linear-gradient(#fff,#f2f2f2);border-bottom:1px solid var(--line)}
.sheet{position:absolute;left:99px;top:119px;width:882px;height:1005px;background:#fff}
.brand{position:absolute;left:101px;top:17px;display:flex;align-items:center;gap:8px}
.brand-mark{width:54px;height:54px;border-radius:50%;background:var(--blue)}
.brand-name{font-family:"Ubuntu",sans-serif;font-size:36px;font-weight:400;color:var(--blue-light);letter-spacing:1px}
.callus{position:absolute;right:102px;top:39px;font-family:"Ubuntu",sans-serif;font-size:16px;color:var(--muted)}
.callus b{font-weight:400;color:var(--blue)}
.nav{position:absolute;left:99px;top:86px;width:882px;height:33px;display:flex;gap:2px}
.nav a{flex:auto;display:flex;align-items:center;justify-content:center;font-size:12px;color:var(--blue-dark);text-decoration:none;background:linear-gradient(#fff,#e9e9e9);border:1px solid var(--line);border-bottom:none;border-radius:4px 4px 0 0}
.nav a.active{background:var(--blue);color:#fff;border-color:var(--blue)}
.news{position:absolute;left:99px;top:119px;width:882px;height:50px;background:linear-gradient(var(--blue),var(--blue-dark));border-radius:0 0 4px 4px;display:flex;align-items:center;color:#fff}
.news h3{font-family:"Ubuntu",sans-serif;font-weight:400;font-size:16px;width:86px;text-align:center;border-right:1px solid rgba(255,255,255,.6);line-height:32px}
.news p{font-size:8.4px;line-height:16px;padding:0 14px 0 16px}
.banner{position:absolute;left:108px;top:180px;width:864px;height:253px;border-radius:8px;border:1px solid var(--line);overflow:hidden;background:linear-gradient(100deg,#c9d3d9 0%,#e6e0da 45%,#f0ece6 60%,#c8cdd2 100%)}
.banner-caption{position:absolute;left:2px;top:77px;width:360px;height:129px;background:rgba(255,255,255,.75);padding:18px 0 0 34px}
.banner-caption h1{font-family:"Ubuntu",sans-serif;font-size:34px;font-weight:500;color:#111;line-height:40px}
.banner-caption h2{font-family:"Ubuntu",sans-serif;font-size:18px;font-weight:400;color:var(--blue);margin-top:4px}
.banner-caption p{font-size:9px;color:var(--blue-dark);margin-top:8px}
.dots{position:absolute;right:12px;bottom:11px;display:flex;gap:2px}
.dots i{width:11px;height:11px;background:var(--blue-light)}
.dots i:first-child{background:#fff}
.features{position:absolute;left:108px;top:450px;width:864px;height:232px;display:flex}
.feature{position:relative;flex:1;background:linear-gradient(var(--blue) 0%,#5aaed6 45%,#fff 100%);border-radius:6px 6px 0 0;text-align:center;color:#fff;border-right:1px solid rgba(255,255,255,.5)}
.feature::after{content:"";position:absolute;right:-9px;top:52px;border-left:9px solid #6bb6dc;border-top:18px solid transparent;border-bottom:18px solid transparent;z-index:2}
.feature:last-child::after{display:none}
.feature h3{font-family:"Ubuntu",sans-serif;font-weight:400;font-size:18px;margin-top:19px}
.feature svg{display:block;margin:14px auto 0}
.feature h4{font-family:"Ubuntu",sans-serif;font-weight:400;font-size:12.5px;color:var(--ink);margin-top:16px}
.feature p{font-size:9.3px;line-height:16px;color:var(--muted);text-align:justify;padding:0 15px;margin-top:8px}
.btn{display:inline-block;margin-top:10px;width:75px;height:20px;line-height:20px;border-radius:5px;background:linear-gradient(#8cc6e2,var(--blue));font-size:9px;color:#fff}
.welcome-title{position:absolute;left:110px;top:720px;font-family:"Ubuntu",sans-serif;font-size:19px;color:var(--blue)}
.video{position:absolute;left:110px;top:755px;width:252px;height:159px;border:2px solid #111;background:linear-gradient(#3a3a3a,#262626)}
.video .bar{position:absolute;left:0;bottom:0;width:100%;height:20px;background:#1b1b1b;color:#ddd;font-size:9px;display:flex;align-items:center;padding-left:55px;gap:14px}
.video .track{width:90px;height:6px;background:#555;position:relative}
.video .track i{position:absolute;left:0;top:0;width:50px;height:6px;background:#888}
.play{position:absolute;left:102px;top:44px;width:52px;height:50px;border-radius:6px;background:rgba(20,20,20,.75)}
.play::after{content:"";position:absolute;left:19px;top:14px;border-left:20px solid var(--blue-light);border-top:11px solid transparent;border-bottom:11px solid transparent}
.welcome-text{position:absolute;left:382px;top:749px;width:254px;font-size:9.3px;line-height:16px;color:var(--muted);text-align:justify}
.welcome-text p+p{margin-top:16px}
.contact{position:absolute;left:656px;top:738px;width:316px;height:167px;border-radius:6px;overflow:hidden;background:linear-gradient(90deg,var(--blue) 0%,var(--blue) 52%,#7fbcd9 70%,#e9dccd 100%);color:#fff;padding:15px 0 0 22px}
.contact-photo{position:absolute;right:0;top:0;width:150px;height:167px;background:linear-gradient(90deg,rgba(30,127,177,0),#ead9c6 60%,#f2e6d8)}
.contact h3{position:relative;font-family:"Ubuntu",sans-serif;font-weight:400;font-size:18px;line-height:22px}
.contact h3 span{display:block;color:var(--blue-light);margin-left:3px}
.contact ul{position:relative;list-style:none;font-family:"Ubuntu",sans-serif;font-size:11px;line-height:16px;margin:6px 0 0 3px}
.contact p{position:relative;font-family:"Ubuntu",sans-serif;font-size:11px;line-height:19px;margin:5px 0 0 3px}
.panels{position:absolute;left:107px;top:933px;width:865px;display:flex;gap:9px}
.panel{flex:1}
.panel-head{height:40px;background:linear-gradient(var(--blue-light),var(--blue));display:flex;align-items:center;gap:18px;padding-left:16px;color:#fff;font-family:"Ubuntu",sans-serif;font-size:19px}
.panel-body{height:92px;background:var(--card);padding:14px 0 0 36px;position:relative}
.panel-body::before{content:"";position:absolute;left:20px;top:20px;border-left:5px solid var(--blue);border-top:3.5px solid transparent;border-bottom:3.5px solid transparent}
.panel-body h4{font-size:14px;font-weight:400;color:var(--blue)}
.panel-body p{font-size:11px;line-height:15px;color:var(--muted);margin-top:6px;width:200px}
.panel-body time{display:block;font-size:11px;color:var(--ink);margin-top:6px}
.panel-foot{height:34px;margin-top:4px;background:var(--card);text-align:right;padding:11px 20px 0 0;font-size:13px;color:var(--blue)}
.footer{position:absolute;left:0;top:1124px;width:1079px;height:76px;background:var(--footer);color:#fff;font-family:"Ubuntu",sans-serif}
.footer-links{position:absolute;left:98px;top:18px;display:flex;font-size:10px}
.footer-links a{color:#fff;text-decoration:none}
.footer-links span{margin:0 20px}
.copy{position:absolute;left:98px;top:45px;font-size:10.5px}
.social{position:absolute;left:927px;top:28px;display:flex;gap:9px}
.social i{width:22px;height:22px;border-radius:50%;background:#6a6a6a}
</style>
</head>
<body>
<div class="topline"></div>
<header class="header"></header>
<div class="sheet"></div>

<div class="brand"><div class="brand-mark"></div><span class="brand-name">KORVA</span></div>
<div class="callus">Call Us : <b>00 0000 000 000</b></div>

<nav class="nav">
  <a class="active" style="flex:0 0 88px">HOME</a>
  <a>ABOUT</a><a>SOLUTIONS</a><a style="flex:0 0 190px">INTELLIGENT DATA CAPTURE</a>
  <a>PRODUCTS</a><a>CUSTOMERS</a><a>FAQ</a><a>CONTACT US</a>
</nav>

<section class="news">
  <h3>News :</h3>
  <p>Lorem Ipsum is simply dummy text of the printing and typesetting industry. Lorem Ipsum has been the industry's standard dummy text ever since the 1500s, when an unknown printer took a galley of type and scrambled it to make a type specimen book.</p>
</section>

<section class="banner" role="img" aria-label="Photo of a smiling businessman with colleagues in an office">
  <div class="banner-caption">
    <h1>KORVA</h1>
    <h2>Intelligent data capture from online sites</h2>
    <p>Lorem Ipsum is simply dummy text of the printing and typesetting industry.</p>
  </div>
  <div class="dots"><i></i><i></i><i></i><i></i><i></i></div>
</section>

<section class="features">
  <article class="feature">
    <h3>Solutions</h3>
    <svg width="66" height="56" viewBox="0 0 66 56" aria-hidden="true"><path fill="#fff" d="M4 12h14a7 7 0 1 1 12 0h14v13a7 7 0 1 1 0 12v13H30a7 7 0 1 0-12 0H4V37a7 7 0 1 0 0-12z"/></svg>
    <h4>Lorem Ipsum is simply dummy</h4>
    <p>Lorem Ipsum is simply dummy text of the printing and typesetting industry. Lorem Ipsum has been the industry's.</p>
    <span class="btn">Readmore</span>
  </article>
  <article class="feature">
    <h3>Intelligent</h3>
    <svg width="66" height="56" viewBox="0 0 66 56" aria-hidden="true"><g fill="#fff"><path d="M21 2h24v5H21zM20 10h26v5H20zM21 18h24v5H21zM22 26h22v5H22z"/><path d="M24 34h18l-3 10H27z"/><rect x="29" y="46" width="8" height="8" rx="2"/></g></svg>
    <h4>Lorem Ipsum is simply dummy</h4>
    <p>Lorem Ipsum is simply dummy text of the printing and typesetting industry. Lorem Ipsum has been the industry's.</p>
    <span class="btn">Readmore</span>
  </article>
  <article class="feature">
    <h3>Products</h3>
    <svg width="66" height="56" viewBox="0 0 66 56" aria-hidden="true"><g fill="none" stroke="#fff" stroke-width="3"><circle cx="33" cy="28" r="25"/><ellipse cx="33" cy="28" rx="11" ry="25"/><path d="M8 28h50M13 15h40M13 41h40"/></g></svg>
    <h4>Lorem Ipsum is simply dummy</h4>
    <p>Lorem Ipsum is simply dummy text of the printing and typesetting industry. Lorem Ipsum has been the industry's.</p>
    <span class="btn">Readmore</span>
  </article>
  <article class="feature">
    <h3>Customers</h3>
    <svg width="66" height="56" viewBox="0 0 66 56" aria-hidden="true"><g fill="#fff"><circle cx="17" cy="12" r="6"/><circle cx="31" cy="10" r="7"/><circle cx="45" cy="12" r="9"/><rect x="9" y="20" width="16" height="14" rx="3"/><rect x="23" y="24" width="16" height="16" rx="3"/><rect x="35" y="23" width="22" height="32" rx="4"/></g></svg>
    <h4>Lorem Ipsum is simply dummy</h4>
    <p>Lorem Ipsum is simply dummy text of the printing and typesetting industry. Lorem Ipsum has been the industry's.</p>
    <span class="btn">Readmore</span>
  </article>
</section>

<h2 class="welcome-title">Welcome to KORVA</h2>
<div class="video" role="img" aria-label="Video still of two businesswomen in a meeting">
  <div class="play"></div>
  <div class="bar"><span>0:04 / 0:30</span><span class="track"><i></i></span></div>
</div>
<div class="welcome-text">
  <p>Lorem Ipsum is simply dummy text of the printing and typesetting industry. Lorem Ipsum has been the industry's standard dummy text ever since the 1500s, when an unknown printer took a galley of type and scrambled.</p>
  <p>It to make a type specimen book. It has survived not only five centuries, but also the leap into electronic typesetting, remaining essentially unchanged. It was popularised in the 1960s with the release of Letraset sheets containing Lorem Ipsum passages, and more recently.</p>
</div>

<aside class="contact">
  <div class="contact-photo" role="img" aria-label="Photo of a smiling support agent on the phone"></div>
  <h3>Contact<span>KORVA</span></h3>
  <ul><li>Lorem Ipsum is simply dummy</li><li>Lorem Ipsum is dummy</li><li>Lorem Ipsum is the simply.</li></ul>
  <p>Call Us : 00 0000 000 000<br>Email Us : korva@info.com</p>
</aside>

<section class="panels">
  <div class="panel">
    <div class="panel-head"><svg width="36" height="32" viewBox="0 0 36 32" aria-hidden="true"><path fill="#fff" d="M2 12l16 10 16-10v18H2z"/><path fill="#fff" d="M11 8l5 5 10-11 3 3-13 14-8-8z"/></svg>Latest News</div>
    <div class="panel-body"><h4>Mauris commodo feugiat</h4><p>Nulla facilisi. Curabitur at elit ligula, eget hendrerit felis vehicula.</p><time>Dec-26-2012</time></div>
    <div class="panel-foot">View All ▸</div>
  </div>
  <div class="panel">
    <div class="panel-head"><svg width="30" height="32" viewBox="0 0 30 32" aria-hidden="true"><g fill="none" stroke="#fff" stroke-width="2"><rect x="2" y="5" width="26" height="25"/><path d="M2 11h26M8 2v6M22 2v6M8 11v19M15 11v19M22 11v19M2 17h26M2 23h26"/></g></svg>Latest Events</div>
    <div class="panel-body"><h4>Mauris commodo feugiat</h4><p>Nulla facilisi. Curabitur at elit ligula, eget hendrerit felis vehicula.</p><time>Dec-26-2012</time></div>
    <div class="panel-foot">View All ▸</div>
  </div>
  <div class="panel">
    <div class="panel-head"><svg width="42" height="30" viewBox="0 0 42 30" aria-hidden="true"><g fill="#fff"><ellipse cx="16" cy="12" rx="15" ry="10"/><path d="M6 18l-3 8 9-5z"/><ellipse cx="29" cy="18" rx="12" ry="8" opacity=".85"/></g></svg>Latest Blog</div>
    <div class="panel-body"><h4>Mauris commodo feugiat</h4><p>Nulla facilisi. Curabitur at elit ligula, eget hendrerit felis vehicula.</p><time>Dec-26-2012</time></div>
    <div class="panel-foot">View All ▸</div>
  </div>
</section>

<footer class="footer">
  <div class="footer-links">
    <a>Home</a><span>|</span><a>About</a><span>|</span><a>Solutions</a><span>|</span><a>intelligent data capture</a><span>|</span><a>Products</a><span>|</span><a>Customers</a><span>|</span><a>Faq</a><span>|</span><a>Contact Us</a>
  </div>
  <div class="copy">Copyright © 2013 &nbsp;www.korva.com &nbsp;All rights reserved.</div>
  <div class="social"><i></i><i></i></div>
</footer>
</body>
</html>
```